CRPG is needing business cards, and stationary created.

Pixel Forge created a logo for our business, and now we are wanting business cards, and stationary. I have included two designs of the same logo. Please feel free to use them as you want. The name of the company is Cedar Ridge Property Group LLC, the address is 812 NE Willow Ln., Suite 9, the city & state is Bend, Oregon, zip code is 97815, Telephone number is 541-327-4489, Fax number is 541-327-6051, the name on the business card is Carl Whitby CMCA

Industry/Entity Type

Property Management

Contact Information for Business Card

The card needs to look professional. Upscale.

Requirements
Must have
• The colors we are using are on the logo that has been uploaded.

```html
<!DOCTYPE html>
<html lang="en">
<head>
<meta charset="utf-8">
<title>Cedar Ridge Property Group – Business Card</title>
<link rel="stylesheet" href="https://fonts.googleapis.com/css2?family=Exo+2:wght@400;600;700&display=swap">
<style>
  :root {
    --teal: #1a8f7c;
    --slate: #3d4a5c;
    --ink: #1f2328;
    --icon: #aeb3b9;
    --paper: #ffffff;
    --backdrop: #e4e5e7;
  }
  * { box-sizing: border-box; margin: 0; padding: 0; }
  html, body { width: 1200px; height: 1200px; overflow: hidden; }
  body {
    background: var(--backdrop);
    font-family: "Exo 2", sans-serif;
    position: relative;
  }
  .card {
    position: absolute;
    width: 700px;
    height: 400px;
    box-shadow: 0 6px 18px rgba(0,0,0,0.12);
  }
  .card-front {
    left: 70px; top: 130px;
    background: var(--teal);
    display: flex; align-items: center; justify-content: center; gap: 22px;
  }
  .brand-mark { width: 34px; height: 34px; }
  .brand-name {
    font-weight: 700; font-size: 64px; letter-spacing: 2px;
    text-transform: uppercase; line-height: 1;
  }
  .card-front .brand-name { color: var(--paper); }
  .card-front .brand-mark { background: var(--paper); }

  .card-back {
    left: 430px; top: 640px;
    background: var(--paper);
    overflow: hidden;
  }
  .back-band { position: absolute; left: 0; bottom: 0; width: 700px; height: 60px; }
  .back-brand {
    position: absolute; left: 40px; top: 190px;
    display: flex; align-items: center; gap: 14px;
  }
  .card-back .brand-name { color: var(--teal); font-size: 40px; }
  .card-back .brand-mark { background: var(--slate); width: 24px; height: 24px; }

  .contact { position: absolute; left: 360px; top: 46px; color: var(--ink); }
  .contact-name { font-weight: 700; font-size: 26px; }
  .contact-role { color: #4f6a8a; font-size: 16px; margin-bottom: 12px; letter-spacing: .5px; }
  .contact-list { list-style: none; }
  .contact-list li {
    display: flex; align-items: center; gap: 10px;
    font-size: 19px; line-height: 30px;
  }
  .contact-list svg { width: 20px; height: 20px; fill: var(--icon); flex: none; }
  .contact-address { font-size: 19px; line-height: 26px; margin-top: 12px; padding-left: 30px; }
</style>
</head>
<body>
  <section class="card card-front">
    <span class="brand-mark"></span>
    <span class="brand-name">Cedar Ridge</span>
  </section>

  <section class="card card-back">
    <div class="back-brand">
      <span class="brand-mark"></span>
      <span class="brand-name">Cedar Ridge</span>
    </div>

    <div class="contact">
      <p class="contact-name">Carl Whitby, CMCA</p>
      <p class="contact-role">POSITION</p>
      <ul class="contact-list">
        <li><svg viewBox="0 0 24 24"><path d="M6.6 10.8a15 15 0 0 0 6.6 6.6l2.2-2.2c.3-.3.7-.4 1-.2 1.1.4 2.3.6 3.6.6.6 0 1 .4 1 1V20c0 .6-.4 1-1 1A17 17 0 0 1 3 4c0-.6.4-1 1-1h3.5c.6 0 1 .4 1 1 0 1.3.2 2.5.6 3.6.1.3 0 .7-.2 1z"/></svg>(541) 327-4489</li>
        <li><svg viewBox="0 0 24 24"><path d="M7 2h9v5H7zM4 8h16c1 0 2 1 2 2v9c0 1-1 2-2 2H4c-1 0-2-1-2-2v-9c0-1 1-2 2-2zm3 4v2h2v-2zm4 0v2h2v-2zm4 0v2h2v-2zm-8 4v2h2v-2zm4 0v2h2v-2zm4 0v2h2v-2z"/></svg>(541) 327-6051</li>
        <li><svg viewBox="0 0 24 24"><path d="M2 5h20v14H2zm2 2v.5l8 5.5 8-5.5V7l-8 5.5z"/></svg>carl@cedarridgepg.com</li>
        <li><svg viewBox="0 0 24 24"><path d="M9 8H6a4 4 0 0 0 0 8h3v-2H6a2 2 0 0 1 0-4h3zm6 0v2h3a2 2 0 0 1 0 4h-3v2h3a4 4 0 0 0 0-8zM8 11h8v2H8z"/></svg>www.cedarridgepg.com</li>
      </ul>
      <p class="contact-address">812 NE Willow Ln., Suite 9,<br>Bend, Oregon 97815</p>
    </div>

    <svg class="back-band" viewBox="0 0 700 60" aria-hidden="true">
      <polygon fill="var(--slate)" points="0,0 30,0 40,18 660,18 670,0 700,0 700,60 0,60"/>
    </svg>
  </section>
</body>
</html>
```